Women's Online Clothing Boutique Needs Business Cards

I already have a logo that I would like to use. Some of the things that interest me is black business cards, foil embossed logo, glossy embossed logo, leopard print, no yellow font, rounded edges. I even like just a large logo on the front side with all of my information on the back side.

Contact Information for Business Card

https://silverheron.shopvenlo.com/
https://www.pagelink.net/thesilverheronboutique/
https://www.picfeed.net/thesilverheronboutique/
silverheronboutique@mailora.net

Requirements
Must have
• My Logo
Nice to have
• Leopard Print
Should not have
• No Yellow Font

```html
<!DOCTYPE html>
<html lang="en">
<head>
<meta charset="utf-8">
<title>The Silver Heron Boutique – Business Cards</title>
<link rel="stylesheet" href="https://fonts.googleapis.com/css2?family=Arimo:wght@400&display=swap">
<style>
  :root {
    --backdrop: #ececec;
    --card-black: #000000;
    --card-white: #ffffff;
    --gold: #c3922e;
    --ink: #111111;
    --white: #ffffff;
  }
  * { margin: 0; padding: 0; box-sizing: border-box; }
  html, body {
    width: 1200px; height: 900px; overflow: hidden;
    background: var(--backdrop);
    font-family: "Arimo", Arial, sans-serif;
  }
  .sheet { position: relative; width: 1200px; height: 900px; }
  .card {
    position: absolute; left: 250px; width: 700px; height: 400px;
    border-radius: 14px; overflow: hidden;
    box-shadow: 0 6px 18px rgba(0,0,0,0.18);
  }
  .card--front { top: 36px; background: var(--card-black); }
  .card--back  { top: 464px; background: var(--card-white); }

  .wordmark {
    position: absolute; left: 0; right: 0;
    text-align: center; font-weight: 400; letter-spacing: 1px;
  }
  .card--front .wordmark {
    top: 170px; font-size: 44px; color: var(--white);
  }
  .card--back .wordmark {
    top: 48px; left: 60px; right: auto; text-align: left;
    font-size: 34px; color: var(--gold);
  }
  .rule { position: absolute; height: 1px; }
  .card--front .rule { background: var(--white); left: 150px; width: 400px; }
  .card--front .rule--top { top: 150px; }
  .card--front .rule--bottom { top: 238px; }
  .card--back .rule { background: var(--gold); left: 60px; width: 420px; top: 100px; }

  .contact-list {
    position: absolute; left: 60px; top: 126px; list-style: none;
    font-size: 17px; color: var(--ink); line-height: 26px;
  }
  .contact-list li { display: flex; align-items: center; gap: 12px; }
  .contact-list li.gap { margin-top: 12px; }
  .icon { width: 18px; height: 18px; flex: none; }
  .social-mark { width: 16px; height: 16px; background: var(--gold); border-radius: 3px; flex: none; margin: 0 1px; }
  .wave { position: absolute; left: 0; bottom: 0; width: 700px; height: 400px; }
  .glow { position: absolute; right: 40px; top: 70px; width: 170px; height: 170px; border-radius: 50%; background: #e6e6e6; }
</style>
</head>
<body>
<main class="sheet">
  <section class="card card--front" aria-label="Card front">
    <div class="rule rule--top"></div>
    <div class="wordmark">The Silver Heron Boutique</div>
    <div class="rule rule--bottom"></div>
  </section>

  <section class="card card--back" aria-label="Card back">
    <div class="glow"></div>
    <svg class="wave" viewBox="0 0 700 400" aria-hidden="true">
      <path d="M0 340 C 200 330, 420 280, 560 170 C 610 130, 660 105, 700 95 L700 400 L0 400 Z" fill="var(--card-black)"/>
      <path d="M0 318 C 190 318, 360 290, 520 190 C 440 260, 260 330, 0 345 Z" fill="var(--gold)"/>
    </svg>
    <div class="wordmark">The Silver Heron Boutique</div>
    <div class="rule"></div>
    <ul class="contact-list">
      <li>
        <svg class="icon" viewBox="0 0 18 18" aria-hidden="true"><rect x="1" y="4" width="16" height="11" fill="var(--gold)"/><path d="M1 4 L9 11 L17 4" stroke="#fff" stroke-width="1.4" fill="none"/></svg>
        silverheronboutique@mailora.net
      </li>
      <li>
        <svg class="icon" viewBox="0 0 18 18" aria-hidden="true"><g fill="none" stroke="var(--gold)" stroke-width="1.4"><circle cx="9" cy="9" r="7.5"/><ellipse cx="9" cy="9" rx="3.3" ry="7.5"/><path d="M1.5 9h15M3 5h12M3 13h12"/></g></svg>
        www.silverheron.shopvenlo.com
      </li>
      <li class="gap"><span class="social-mark"></span>www.pagelink.net/thesilverheronboutique</li>
      <li><span class="social-mark"></span>www.picfeed.net/thesilverheronboutique</li>
    </ul>
  </section>
</main>
</body>
</html>
```